Business Card Design

We just need these details on one side of card and logo on the other.

Industry/Entity Type

Business

Contact Information for Business Card

Lisel Pardoe | Artist
118 Coldwell Street
Brenton Park Vic 3172
# 0412 978 205 | 03 9187 2604
lisel@liselpardoe.com
liselsnook.com.au

```html
<!DOCTYPE html>
<html lang="en">
<head>
<meta charset="utf-8">
<title>Lisel's Nook — Business Card</title>
<link href="https://fonts.googleapis.com/css2?family=Lato:wght@400;700&display=swap" rel="stylesheet">
<style>
  :root {
    --backdrop: #d9d9d9;
    --ink: #000000;
    --paper: #ffffff;
    --accent: #e8a92e;
    --card-w: 700px;
    --card-h: 400px;
  }
  * { box-sizing: border-box; margin: 0; padding: 0; }
  html, body {
    width: 1200px; height: 926px; overflow: hidden;
    background: var(--backdrop);
    font-family: "Lato", Arial, sans-serif;
  }
  .sheet {
    width: 1200px; height: 926px;
    display: flex; flex-direction: column;
    align-items: center; justify-content: center; gap: 42px;
  }
  .card {
    width: var(--card-w); height: var(--card-h);
    position: relative;
    box-shadow: 0 2px 8px rgba(0,0,0,.18);
  }

  /* Logo side */
  .card--front {
    background: var(--ink); color: var(--paper);
    display: flex; flex-direction: column; align-items: center; justify-content: center;
  }
  .brand-name {
    font-weight: 700; font-size: 74px; letter-spacing: 1px; line-height: 1;
    white-space: nowrap;
  }
  .brand-tagline {
    margin-top: 14px; font-size: 17px; letter-spacing: 4px; font-weight: 400;
    white-space: nowrap;
  }
  .brand-url {
    margin-top: 40px; font-size: 21px; letter-spacing: 3.5px;
  }

  /* Details side */
  .card--back { background: var(--paper); }
  .back-logo {
    position: absolute; left: 30px; top: 22px; color: var(--ink);
  }
  .back-logo .brand-name { font-size: 34px; letter-spacing: .5px; }
  .back-logo .brand-tagline { margin-top: 4px; font-size: 9px; letter-spacing: 2px; font-weight: 700; }
  .detail-bands {
    position: absolute; left: 22px; right: 22px; top: 96px;
    list-style: none; display: flex; flex-direction: column; gap: 6px;
  }
  .band {
    height: 36px; background: var(--ink); color: var(--paper);
    display: flex; align-items: center; justify-content: flex-end;
    padding: 0 14px; font-size: 21px; font-weight: 700; letter-spacing: 1.5px;
    white-space: nowrap; overflow: hidden;
  }
  .band--name { color: var(--accent); letter-spacing: 2.5px; }
  .band--email { font-weight: 400; letter-spacing: 1px; }
  .band--address {
    justify-content: flex-start; font-weight: 400; font-size: 19px; letter-spacing: 1.2px;
  }
</style>
</head>
<body>
<main class="sheet">
  <section class="card card--front" aria-label="Card front">
    <div class="brand-name">Lisel's Nook</div>
    <div class="brand-tagline">STUDIO · CAFE · GALLERY</div>
    <div class="brand-url">www.liselsnook.com.au</div>
  </section>

  <section class="card card--back" aria-label="Card back">
    <div class="back-logo">
      <div class="brand-name">Lisel's Nook</div>
      <div class="brand-tagline">STUDIO · CAFE · GALLERY</div>
    </div>
    <ul class="detail-bands">
      <li class="band"></li>
      <li class="band"></li>
      <li class="band band--name">LISEL PARDOE</li>
      <li class="band">0412 978 205</li>
      <li class="band">03 9187 2604</li>
      <li class="band band--email">lisel@liselpardoe.com</li>
      <li class="band band--address">Artist 118 Coldwell Street Brenton Park Vic 3172</li>
    </ul>
  </section>
</main>
</body>
</html>
```